Harbor Glow Living.com Landing Page

Create a well designed home/landing page using that communicates the feeling of Harbor Glow Living with this sections that scroll from top to bottom -
Top section - Displays "Harbor Glow Living" with space for embedded YouTube video.

The following sections follow the top section -
Assess your current Harbor Glow Living. Complete our free life balance assessment to identify key areas where you you will most benefit.
"Learn more" call to action button

Create a Harbor Glow Living Study Hub account. Get a 14 day free trial to a wealth of learning activities, motivational videos and professional presentations on our learning portal designed specifically to address the eight essential areas of Harbor Glow Living.
"Register now" call to action button

Get weekly reports on your progress and goal achievement. Celebrate your success each week as you review your progress on each life balance area.

Appropriate royalty free photos and graphics that fit the chosen theme you recommend.
Updates

I'm reviewing the designs. I realize that I need to clarify that Harbor Glow Living focuses on eight areas, not just physical fitness and meditation. Spirituality and Sense of Purpose; Fitness and Health; Relationships; Personal Finance; Recreation and Fun; Physical Environment; Personal Development and Learning; Work and Career

Number of Pages Required

1 page

Colors
33a6d7
00a990
9bcb3c
2f73b3

```html
<!DOCTYPE html>
<html lang="en">
<head>
<meta charset="UTF-8">
<title>Harbor Glow Living</title>
<link rel="stylesheet" href="https://fonts.googleapis.com/css2?family=Montserrat:wght@600;700;800&family=Barlow:wght@400&display=swap">
<style>
  :root {
    --sky: #33a6d7;
    --teal: #00a990;
    --lime: #9bcb3c;
    --ocean: #2f73b3;
    --btn-blue: #2a8fd0;
    --btn-green: #86c232;
    --btn-teal: #17a08a;
    --footer: #333333;
    --white: #ffffff;
  }
  * { margin: 0; padding: 0; box-sizing: border-box; }
  html, body { width: 1200px; height: 2234px; overflow: hidden; }
  body { font-family: "Montserrat", sans-serif; color: var(--white); background: var(--footer); }
  .page { position: relative; width: 1200px; height: 2234px; }
  section, footer { position: absolute; left: 0; width: 1200px; overflow: hidden; }
  .photo { position: absolute; inset: 0; }

  .hero { top: 0; height: 651px; }
  .hero .photo {
    background: linear-gradient(100deg, #2fa3d9 0%, #1fb98f 40%, #52c067 65%, #8fcb3f 100%);
  }
  .hero .photo::after {
    content: ""; position: absolute; left: 0; right: 0; bottom: 0; height: 80px;
    background: linear-gradient(to bottom, rgba(47,115,179,0) 0%, rgba(47,115,179,0.25) 100%);
  }
  .menu-toggle { position: absolute; left: 1062px; top: 33px; width: 62px; height: 36px; }
  .menu-toggle span { position: absolute; left: 0; width: 62px; height: 6px; border-radius: 3px; background: var(--white); }
  .menu-toggle span:nth-child(1) { top: 0; }
  .menu-toggle span:nth-child(2) { top: 15px; }
  .menu-toggle span:nth-child(3) { top: 30px; }
  .hero-title {
    position: absolute; top: 196px; left: 0; width: 1200px; text-align: center;
    font-weight: 800; font-size: 88px; line-height: 84px; letter-spacing: -0.5px;
  }
  .play-button { position: absolute; left: 559px; top: 405px; width: 82px; height: 82px; }

  .feature .copy { position: absolute; font-weight: 600; }
  .btn {
    position: absolute; display: inline-flex; align-items: center; justify-content: center;
    border-radius: 20px; font-weight: 700; font-size: 13px; color: var(--white);
    text-decoration: none; letter-spacing: 0.2px;
  }

  .assess { top: 651px; height: 486px; }
  .assess .photo {
    background: linear-gradient(to bottom, #7cc1e8 0%, #6aa7c9 25%, #3f7d8a 50%, #2e6a3c 78%, #2c5a2a 88%, #8a7d72 90%, #6e6258 100%);
  }
  .assess .copy { left: 172px; top: 105px; width: 520px; font-size: 31px; line-height: 36px; }
  .assess .btn { left: 172px; top: 303px; width: 129px; height: 40px; background: var(--btn-blue); }

  .portal { top: 1137px; height: 484px; }
  .portal .photo {
    background: linear-gradient(to bottom, #1f3a1c 0%, #2f5a26 40%, #4d7d2c 70%, #9cc23a 88%, #6c9a25 100%);
  }
  .portal .copy { left: 539px; top: 118px; width: 500px; font-size: 21px; line-height: 25px; }
  .portal .btn { left: 539px; top: 318px; width: 151px; height: 39px; background: var(--btn-green); }

  .reports { top: 1621px; height: 482px; }
  .reports .photo {
    background: linear-gradient(to bottom, #4fa7a0 0%, #6fb7b0 25%, #b6cfd0 50%, #c9d6d8 70%, #8fc0c2 90%, #3a9aa0 100%);
  }
  .reports .copy { left: 172px; top: 100px; width: 520px; font-size: 29px; line-height: 34px; }
  .reports .btn { left: 172px; top: 300px; width: 129px; height: 40px; background: var(--btn-teal); }

  .site-footer { top: 2103px; height: 131px; background: var(--footer); text-align: center; }
  .copyright { position: absolute; top: 37px; left: 0; width: 1200px; font-family: "Barlow", sans-serif; font-size: 12px; }
  .social { position: absolute; top: 73px; left: 0; width: 1200px; display: flex; justify-content: center; gap: 15px; }
  .social a { display: block; width: 18px; height: 18px; border-radius: 50%; background: var(--white); }
</style>
</head>
<body>
<div class="page">

  <section class="hero">
    <div class="photo" role="img" aria-label="Woman with arms raised facing the sea, under a blue-to-green colour wash"></div>
    <div class="menu-toggle" aria-label="Menu"><span></span><span></span><span></span></div>
    <h1 class="hero-title">Harbor Glow<br>Living</h1>
    <svg class="play-button" viewBox="0 0 82 82" aria-label="Play video">
      <circle cx="41" cy="41" r="39" fill="none" stroke="#ffffff" stroke-width="3"/>
      <path d="M32 25 L58 41 L32 57 Z" fill="#ffffff"/>
    </svg>
  </section>

  <section class="feature assess">
    <div class="photo" role="img" aria-label="Woman in yoga pose on a wooden deck overlooking forested mountains"></div>
    <p class="copy">Assess your current Harbor Glow Living. Complete our free life balance assessment to identify key areas where you you will most benefit.</p>
    <a class="btn" href="#">LEARN MORE</a>
  </section>

  <section class="feature portal">
    <div class="photo" role="img" aria-label="Woman meditating cross-legged on grass in a sunlit forest"></div>
    <p class="copy">Create a Harbor Glow Living Study Hub account. Get a 14 day free trial to a wealth of learning activities, motivational videos and professional presentations on our learning portal designed specifically to address the eight essential areas of Harbor Glow Living.</p>
    <a class="btn" href="#">REGISTER NOW</a>
  </section>

  <section class="feature reports">
    <div class="photo" role="img" aria-label="Woman relaxing at the edge of an infinity pool with a lake behind"></div>
    <p class="copy">Get weekly reports on your progress and goal achievement. Celebrate your success each week as you review your progress on each life balance area.</p>
    <a class="btn" href="#">LEARN MORE</a>
  </section>

  <footer class="site-footer">
    <p class="copyright">Copyright 2020 All Rights Reserved</p>
    <nav class="social" aria-label="Social links">
      <a href="#" aria-label="Social link 1"></a>
      <a href="#" aria-label="Social link 2"></a>
      <a href="#" aria-label="Social link 3"></a>
      <a href="#" aria-label="Social link 4"></a>
      <a href="#" aria-label="Social link 5"></a>
    </nav>
  </footer>

</div>
</body>
</html>
```